Mosk trail Website

We need a simple web page design for our businessWe procure and dispose of earthmoving construction equipmentwe also find construction equipment for our customers using our global contacts

Number of Pages Required

1 page

```html
<!DOCTYPE html>
<html lang="en">
<head>
<meta charset="utf-8">
<title>Mosk trail</title>
<link rel="stylesheet" href="https://fonts.googleapis.com/css2?family=Maven+Pro:wght@400;500;700&family=Open+Sans:wght@400;600&display=swap">
<style>
  :root {
    --orange: #f7941d;
    --dark: #272727;
    --white: #ffffff;
    --text: #222222;
    --muted: #cfcfcf;
    --sky-top: #0a2250;
    --sky: #3f7fc8;
    --earth: #8a4a22;
  }
  * { box-sizing: border-box; margin: 0; padding: 0; }
  html, body { width: 1200px; height: 2605px; overflow: hidden; background: var(--white); }
  body { position: relative; font-family: "Open Sans", sans-serif; color: var(--text); }
  .abs { position: absolute; }
  .heading { font-family: "Maven Pro", sans-serif; font-weight: 500; color: var(--orange); text-transform: uppercase; white-space: nowrap; }
  .btn {
    position: absolute; background: var(--orange); color: var(--text);
    font-family: "Maven Pro", sans-serif; font-size: 15px; text-transform: uppercase;
    display: flex; align-items: center; justify-content: center; border-radius: 2px;
  }

  /* Hero */
  .hero {
    position: absolute; left: 0; top: 0; width: 1200px; height: 747px;
    clip-path: polygon(0 0, 1200px 0, 1200px 625px, 1077px 747px, 122px 747px, 0 625px);
  }
  .hero-photo {
    position: absolute; inset: 0;
    background: linear-gradient(180deg, var(--sky-top) 0%, var(--sky) 35%, #b07a4a 55%, var(--earth) 100%);
  }
  .logo { left: 144px; top: 16px; font-family: "Maven Pro", sans-serif; font-weight: 700; font-size: 37px; color: var(--orange); text-transform: uppercase; letter-spacing: 0.5px; }
  .nav { right: 146px; top: 29px; display: flex; gap: 37px; list-style: none; }
  .nav li { font-family: "Maven Pro", sans-serif; font-size: 14px; color: var(--white); text-transform: uppercase; }
  .nav li.active { color: var(--orange); }
  .hero-title { left: 0; width: 1200px; top: 152px; text-align: center; color: var(--white); font-family: "Maven Pro", sans-serif; font-size: 31px; line-height: 41px; text-transform: uppercase; font-weight: 500; }
  .hero .btn { left: 531px; top: 243px; width: 136px; height: 38px; font-weight: 700; box-shadow: 0 2px 6px rgba(0,0,0,.3); }
  .arrow { top: 292px; }

  /* Welcome */
  .welcome-title { left: 144px; top: 815px; font-size: 40px; }
  .welcome-text { left: 144px; top: 876px; width: 495px; font-size: 12.8px; line-height: 23.8px; }
  .welcome .btn { left: 144px; top: 1063px; width: 111px; height: 38px; }
  .welcome-photo { left: 679px; top: 827px; width: 377px; height: 274px; background: linear-gradient(180deg, #3a4658 0%, #7a5a3e 55%, #231a14 100%); }

  /* Services */
  .services {
    position: absolute; left: 0; top: 1181px; width: 1200px; height: 497px; background: var(--dark);
    clip-path: polygon(0 0, 1200px 0, 1200px 373px, 1087px 497px, 113px 497px, 0 373px);
  }
  .services-title { left: 0; width: 1200px; top: 70px; text-align: center; font-size: 40px; }
  .service-card { position: absolute; top: 142px; width: 217px; }
  .service-photo { width: 217px; height: 200px; }
  .service-label { height: 63px; background: var(--orange); color: var(--text); font-family: "Maven Pro", sans-serif; font-weight: 500; font-size: 21px; line-height: 21px; text-transform: uppercase; text-align: center; display: flex; align-items: center; justify-content: center; }
  .p1 { background: linear-gradient(180deg, #4a5e7a 0%, #8a7440 100%); }
  .p2 { background: linear-gradient(180deg, #8a9ab0 0%, #a8702a 100%); }
  .p3 { background: linear-gradient(180deg, #4a5472 0%, #8a4a24 100%); }
  .p4 { background: linear-gradient(180deg, #6a5a40 0%, #8a6a3a 100%); }

  /* Reviews */
  .reviews-title { left: 0; width: 1200px; top: 1750px; text-align: center; font-size: 40px; }
  .quote { left: 140px; width: 920px; top: 1800px; text-align: center; font-size: 16px; line-height: 24.5px; }
  .reviewer { left: 0; width: 1200px; top: 1879px; text-align: center; font-family: "Maven Pro", sans-serif; font-size: 21px; }
  .dots { left: 554px; top: 1921px; }

  /* Contact */
  .contact {
    position: absolute; left: 0; top: 2015px; width: 1200px; height: 494px; background: var(--dark);
    clip-path: polygon(113px 0, 1087px 0, 1200px 121px, 1200px 494px, 0 494px, 0 121px);
  }
  .contact-title { left: 0; width: 1200px; top: 70px; text-align: center; font-size: 40px; }
  .contact-line { left: 0; width: 1200px; top: 120px; text-align: center; color: var(--white); font-family: "Maven Pro", sans-serif; font-size: 18px; display: flex; justify-content: center; align-items: center; gap: 8px; }
  .field { position: absolute; top: 166px; width: 217px; height: 38px; background: var(--white); font-size: 12px; color: #777; padding: 11px 16px; }
  .field.select svg { position: absolute; right: 14px; top: 16px; }
  .message { position: absolute; left: 144px; top: 225px; width: 912px; height: 127px; background: var(--white); font-size: 12px; color: #777; padding: 14px 16px; }
  .contact .btn { left: 544px; top: 373px; width: 112px; height: 40px; }

  /* Footer */
  .footer { position: absolute; left: 0; top: 2509px; width: 1200px; height: 96px; background: var(--orange); }
  .footer-links { left: 144px; top: 22px; font-family: "Maven Pro", sans-serif; font-size: 14px; font-weight: 500; color: var(--text); }
  .footer-links span { margin: 0 10px; }
  .copyright { left: 144px; top: 49px; font-family: "Maven Pro", sans-serif; font-size: 13px; font-weight: 500; }
  .social { left: 981px; top: 30px; display: flex; gap: 8px; }
  .social span { width: 32px; height: 32px; border-radius: 50%; background: var(--dark); display: block; }
</style>
</head>
<body>

<header class="hero">
  <div class="hero-photo" role="img" aria-label="Photo of an excavator digging earth under a blue sky"></div>
  <div class="abs logo">Mosk trail</div>
  <ul class="abs nav">
    <li class="active">Home</li><li>About Us</li><li>Services</li><li>Reviews</li><li>Contact Us</li>
  </ul>
  <h1 class="abs hero-title">We procure and dispose of<br>earthmoving construction equipment.</h1>
  <div class="btn">Contact Us</div>
  <svg class="abs arrow" style="left:54px" width="22" height="30" viewBox="0 0 22 30"><path d="M16 3 L5 15 L16 27" fill="none" stroke="#fff" stroke-width="4"/></svg>
  <svg class="abs arrow" style="left:1122px" width="22" height="30" viewBox="0 0 22 30"><path d="M6 3 L17 15 L6 27" fill="none" stroke="#fff" stroke-width="4"/></svg>
</header>

<section class="welcome">
  <h2 class="abs heading welcome-title">Welcome to Mosk trail</h2>
  <p class="abs welcome-text">Fusce sollicitudin lorem et luctus volutpat. Proin placerat dapibus gravida. In tristique nulla eget hendrerit. Maecenas vel tortor accumsan quam varius imperdiet vel eget elit. Aenean facilisis tincidunt lectus, id dictum nisi luctus eget. Vivamus efficitur ex condimentum, malesuada eros eget, feugiat nibh. Sed tellus ex, imperdiet eget gravida sit amet, volutpat eget turpis. In nec ultricies est. Etiam mattis augue vehicula odio posuere, sit amet tempus lectus luctus. Nulla facilisi. Etiam vel massa elementum, bibendum tellus venenatis, feugiat massa.</p>
  <div class="btn">Read More</div>
  <div class="abs welcome-photo" role="img" aria-label="Photo of two excavators at sunset"></div>
</section>

<section class="services">
  <h2 class="abs heading services-title">Services</h2>
  <div class="service-card" style="left:144px"><div class="service-photo p1" role="img" aria-label="Photo of a row of dump trucks"></div><div class="service-label">Procure</div></div>
  <div class="service-card" style="left:375px"><div class="service-photo p2" role="img" aria-label="Photo of a mining haul truck"></div><div class="service-label">Dispose</div></div>
  <div class="service-card" style="left:608px"><div class="service-photo p3" role="img" aria-label="Photo of construction vehicles at sunset"></div><div class="service-label">Construction<br>Vehicles</div></div>
  <div class="service-card" style="left:839px"><div class="service-photo p4" role="img" aria-label="Photo of safety gear on a workbench"></div><div class="service-label">Construction<br>Equipment</div></div>
</section>

<section class="reviews">
  <h2 class="abs heading reviews-title">Reviews</h2>
  <p class="abs quote">" Vivamus eleifend vitae nulla vel malesuada. In ac malesuada lacus, et consectetur ante. Fusce vitae lectus sit amet mi pulvinar maximus. Aenean placerat, nibh vel accumsan aliquet, magna nibh accumsan nibh, ac tempus nunc ipsum ac tellus. Cras augue magna, placerat eget nulla. "</p>
  <p class="abs reviewer">Ray Dunn, Phasellus nisl</p>
  <svg class="abs dots" width="92" height="14" viewBox="0 0 92 14">
    <circle cx="7" cy="7" r="6" fill="#f7941d"/><circle cx="31" cy="7" r="6" fill="#cfcfcf"/><circle cx="55" cy="7" r="6" fill="#cfcfcf"/><circle cx="79" cy="7" r="6" fill="#cfcfcf"/>
  </svg>
</section>

<section class="contact">
  <h2 class="abs heading contact-title">Contact Us</h2>
  <div class="abs contact-line">
    <svg width="14" height="11" viewBox="0 0 14 11"><rect x="0" y="0" width="14" height="11" fill="#fff"/><path d="M0 0 L7 6 L14 0" fill="none" stroke="#272727" stroke-width="1.5"/></svg>
    <span>dean@mosktrail.com.au</span><span>&nbsp;&nbsp;/&nbsp;&nbsp;</span>
    <svg width="12" height="12" viewBox="0 0 12 12"><path d="M2 1 L4.5 1 L5.5 3.5 L4 4.8 Q5.2 7.2 7.3 8 L8.5 6.5 L11 7.5 L11 10 Q10 11.5 8 11 Q2 9 1 3 Q0.8 1.5 2 1 Z" fill="#fff"/></svg>
    <span>0400 182 640</span>
  </div>
  <div class="field" style="left:144px">Name</div>
  <div class="field" style="left:375px">Email</div>
  <div class="field" style="left:608px">Phone</div>
  <div class="field select" style="left:839px">Service for<svg width="10" height="6" viewBox="0 0 10 6"><path d="M0 0 L10 0 L5 6 Z" fill="#555"/></svg></div>
  <div class="message">Message</div>
  <div class="btn">Read More</div>
</section>

<footer class="footer">
  <div class="abs footer-links">Home<span>|</span>About Us<span>|</span>Services<span>|</span>Reviews<span>|</span>Contact Us</div>
  <div class="abs copyright">Copyright &copy; 2018 Mosk trail. &nbsp;All rights reserved.</div>
  <div class="abs social"><span></span><span></span></div>
</footer>

</body>
</html>
```